7 P's for Healthcare Companies - Textbook Graphic

Can you create a graphic for me for a medical textbook? The goal is to show 7 critical features of a healthcare startup and the audience is physicians with limited business backgrounds.

Please include a picture of young, male emergency physician in the middle of the graphic. Show them evaluating an idea. Can you surround the physician with bold writing for the seven components, and use brief descriptions and simple images or graphics to illustrate the point?

The image should be somewhat formal, but it's OK to be lighthearded.

The seven P's and brief descriptions include the following:
Product: what is their market solution?
(Intellectual) Property: do they have a patent or trademark?
Product Clearance: how will they get QRB approval and TPW clearance?
Payment: how will they make money?
Pilots: have they applied their product in a healthcare setting?
Physician and Patient feedback: Do doctors and patients like their product?
Publication: do they have evidence their product works?

More detail and information is available at this website: https://brenvolt.com/blog/uncategorized/healthcare-framework/

I will need to own this image

```html
<!DOCTYPE html>
<html lang="en">
<head>
<meta charset="utf-8">
<title>7P's to Evaluate the Healthcare Companies</title>
<link href="https://fonts.googleapis.com/css2?family=Bebas+Neue&display=swap" rel="stylesheet">
<style>
  :root {
    --brand-blue: #1b56a1;
    --brand-blue-deep: #174a8c;
    --paper: #ffffff;
    --stage: #ffffff;
    --sky: #dcedf9;
    --sky-mid: #c3e1ee;
    --aqua: #9fd7ec;
    --aqua-light: #b4f4fb;
    --badge: #f7ec19;
    --ink: #111111;
    --coat: #fbfbfb;
    --coat-shade: #e6eaee;
  }
  * { box-sizing: border-box; margin: 0; padding: 0; }
  html, body { width: 1200px; height: 1143px; overflow: hidden; background: var(--stage); }
  body { position: relative; font-family: "Bebas Neue", "Oswald", sans-serif; }

  .poster {
    position: absolute; left: 243px; top: 123px;
    width: 718px; height: 898px; overflow: hidden;
    background: var(--sky);
  }
  .top-band { position: absolute; left: 0; top: 0; width: 100%; height: 133px; background: var(--brand-blue); }
  .clinic-scene {
    position: absolute; left: 0; top: 133px; width: 100%; height: 765px;
    background: linear-gradient(180deg, var(--sky) 0%, var(--sky) 35%, var(--sky-mid) 55%, var(--aqua) 78%, var(--aqua-light) 88%, var(--aqua) 100%);
  }
  .physician {
    position: absolute; left: 215px; top: 166px; width: 280px; height: 732px;
    border-radius: 110px 110px 0 0;
    background: linear-gradient(180deg, var(--coat-shade) 0%, var(--coat) 40%, var(--coat) 100%);
  }

  .header-card {
    position: absolute; left: 18px; top: 21px; width: 683px; height: 170px;
    background: var(--paper); border: 2.5px solid var(--brand-blue); border-radius: 32px;
  }
  .header-mark {
    position: absolute; left: 28px; top: 21px; width: 204px; height: 124px;
    background: var(--brand-blue); border-radius: 8px;
    color: var(--paper); font-size: 124px; line-height: 1;
    display: flex; align-items: center; justify-content: center; padding-top: 10px;
  }
  .header-title {
    position: absolute; left: 259px; top: 36px;
    color: var(--brand-blue); font-size: 52px; line-height: 55px; font-weight: 400;
    letter-spacing: -0.5px; white-space: nowrap;
  }

  .p-card {
    position: absolute; width: 160px;
    background: var(--brand-blue); border: 1.5px solid var(--paper); border-radius: 6px;
    padding: 8px 7px 6px;
    display: flex; flex-direction: column; align-items: center;
  }
  .p-card__label {
    width: 100%; background: var(--paper); border-radius: 3px;
    color: var(--brand-blue); font-size: 31px; line-height: 33px; font-weight: 400;
    letter-spacing: -0.4px; white-space: nowrap;
    text-align: center; padding: 5px 2px 1px;
  }
  .p-card__question {
    flex: 1; display: flex; align-items: center; justify-content: center;
    color: var(--paper); font-size: 17px; line-height: 21px; text-align: center;
    letter-spacing: -0.2px; white-space: nowrap;
    padding-top: 4px;
  }
  .p-card__number {
    position: absolute; top: -10px; right: -10px; width: 25px; height: 25px;
    border-radius: 50%; background: var(--badge); border: 2px solid var(--brand-blue-deep);
    color: var(--ink); font-family: Arial, sans-serif; font-size: 16px; font-weight: 700;
    display: flex; align-items: center; justify-content: center;
  }
  .p-card--left { left: 40px; }
  .p-card--right { left: 511px; }
</style>
</head>
<body>
  <main class="poster">
    <div class="top-band"></div>
    <div class="clinic-scene" role="img" aria-label="Soft illustrated hospital room background with IV stand, cabinets and bed"></div>
    <div class="physician" role="img" aria-label="Illustration of a smiling young male physician in a white coat with a stethoscope, arms crossed"></div>

    <header class="header-card">
      <div class="header-mark">7P’S</div>
      <h1 class="header-title">TO EVALUATE THE<br>HEALTHCARE COMPANIES</h1>
    </header>

    <section class="p-card p-card--left" style="top:238px;height:115px;">
      <span class="p-card__number">1</span>
      <h2 class="p-card__label">PRODUCT</h2>
      <p class="p-card__question">WHAT IS THEIR<br>MARKET SOLUTION ?</p>
    </section>

    <section class="p-card p-card--left" style="top:390px;height:115px;">
      <span class="p-card__number">2</span>
      <h2 class="p-card__label">PROPERTY</h2>
      <p class="p-card__question">DO THEY HAVE A PATENT<br>OR TRADEMARK ?</p>
    </section>

    <section class="p-card p-card--left" style="top:541px;height:177px;">
      <span class="p-card__number">3</span>
      <h2 class="p-card__label">PRODUCT<br>CLEARANCE</h2>
      <p class="p-card__question">HOW WILL THEY GET<br>QRB APPROVAL AND<br>TPW CLEARANCE ?</p>
    </section>

    <section class="p-card p-card--left" style="top:751px;height:100px;">
      <span class="p-card__number">4</span>
      <h2 class="p-card__label">PAYMENT</h2>
      <p class="p-card__question">WILL THEY MAKE MONEY ?</p>
    </section>

    <section class="p-card p-card--right" style="top:238px;height:154px;">
      <span class="p-card__number">5</span>
      <h2 class="p-card__label">PILOTS</h2>
      <p class="p-card__question">HAVE THEY APPLIED<br>THEIR PRODUCT IN A<br>HEALTHCARE SETTING ?</p>
    </section>

    <section class="p-card p-card--right" style="top:429px;height:233px;">
      <span class="p-card__number">6</span>
      <h2 class="p-card__label">PHYSICIAN<br>AND PATIENT<br>FEEDBACK</h2>
      <p class="p-card__question">DO DOCTORS AND<br>PATIENTS LIKE<br>THEIR PRODUCT ?</p>
    </section>

    <section class="p-card p-card--right" style="top:703px;height:148px;">
      <span class="p-card__number">7</span>
      <h2 class="p-card__label">PUBLICATION</h2>
      <p class="p-card__question">DO THEY HAVE<br>EVIDENCE THEIR<br>PRODUCT WORKS ?</p>
    </section>
  </main>
</body>
</html>
```